Business card for my company-RKV Design Studio

I do not have a logo-I like red and keeping it clean. Information that should be on the card:
Tom Brazenhall AIA
Architecture Planning Interiors
Cell Phone-614.529.4086
email-rkvplanner4@mailvane.net
www.rkvdesignstudio.net

```html
<!DOCTYPE html>
<html lang="en">
<head>
<meta charset="utf-8">
<title>RKV Design Studio — Business Card</title>
<link href="https://fonts.googleapis.com/css2?family=PT+Serif:wght@400;700&display=swap" rel="stylesheet">
<style>
  :root {
    --backdrop: #2a2a2c;
    --brand-red: #e01b22;
    --brand-red-deep: #c9161d;
    --logo-red: #a3141b;
    --ink-grey: #4a4a4a;
    --card-white: #f7f7f7;
    --blush: #f6e3e4;
    --monogram-tint: #ecd3d5;
  }
  * { margin: 0; padding: 0; box-sizing: border-box; }
  html, body {
    width: 1200px; height: 900px; overflow: hidden;
    background: var(--backdrop);
    font-family: "PT Serif", Georgia, serif;
  }
  .canvas { position: relative; width: 1200px; height: 900px; }
  .card {
    position: absolute; left: 250px; width: 700px; height: 400px;
    border-radius: 36px; overflow: hidden;
    box-shadow: 0 14px 30px rgba(0,0,0,0.45);
  }
  .card--front {
    top: 40px;
    background: linear-gradient(135deg, var(--brand-red-deep) 0%, var(--brand-red) 60%, #e8242a 100%);
    display: flex; align-items: center; justify-content: center; gap: 14px;
  }
  .brand-mark { width: 22px; height: 22px; background: #ffffff; }
  .brand-name { color: #ffffff; font-weight: 700; font-size: 40px; letter-spacing: 0.5px; }

  .card--back {
    top: 460px;
    background: linear-gradient(110deg, #ececec 0%, var(--card-white) 40%, var(--blush) 100%);
  }
  .monogram-field {
    position: absolute; left: 250px; top: 40px; width: 380px; height: 360px;
    background: linear-gradient(160deg, var(--monogram-tint) 0%, #f0dcde 100%);
    opacity: 0.8; border-radius: 24px 24px 0 0;
  }
  .back-brand {
    position: absolute; left: 36px; top: 170px;
    display: flex; align-items: center; gap: 10px;
  }
  .back-brand .brand-mark { width: 16px; height: 16px; background: var(--logo-red); }
  .back-brand .brand-name { color: var(--logo-red); font-size: 28px; }
  .divider {
    position: absolute; left: 370px; top: 160px; width: 1.5px; height: 170px;
    background: var(--logo-red);
  }
  .contact-block { position: absolute; left: 392px; top: 150px; }
  .person-name { color: var(--brand-red); font-weight: 700; font-size: 26px; line-height: 1.1; }
  .person-title { color: var(--ink-grey); font-size: 17px; margin-top: 4px; }
  .contact-list { list-style: none; margin-top: 24px; }
  .contact-list li {
    display: flex; align-items: center; gap: 10px;
    color: var(--ink-grey); font-size: 17px; line-height: 1; margin-bottom: 13px;
  }
  .contact-list svg { width: 15px; height: 15px; flex: none; }
</style>
</head>
<body>
<main class="canvas">
  <section class="card card--front">
    <span class="brand-mark"></span>
    <span class="brand-name">RKV Design Studio</span>
  </section>

  <section class="card card--back">
    <div class="monogram-field" role="img" aria-label="Faint oversized brand monogram decoration"></div>
    <div class="back-brand">
      <span class="brand-mark"></span>
      <span class="brand-name">RKV Design Studio</span>
    </div>
    <div class="divider"></div>
    <div class="contact-block">
      <p class="person-name">Tom Brazenhall AIA</p>
      <p class="person-title">Architecture Planning Interiors</p>
      <ul class="contact-list">
        <li>
          <svg viewBox="0 0 16 16" aria-hidden="true"><rect x="4" y="1" width="8" height="14" rx="1.5" fill="none" stroke="#e01b22" stroke-width="1.5"/><circle cx="8" cy="12.5" r="0.9" fill="#e01b22"/></svg>
          614.529.4086
        </li>
        <li>
          <svg viewBox="0 0 16 16" aria-hidden="true"><rect x="1" y="3" width="14" height="10" rx="1" fill="#e01b22"/><path d="M1.5 3.5 L8 9 L14.5 3.5" fill="none" stroke="#fff" stroke-width="1.2"/></svg>
          rkvplanner4@mailvane.net
        </li>
        <li>
          <svg viewBox="0 0 16 16" aria-hidden="true"><circle cx="8" cy="8" r="7" fill="#e01b22"/><ellipse cx="8" cy="8" rx="3" ry="7" fill="none" stroke="#fff" stroke-width="1"/><line x1="1" y1="8" x2="15" y2="8" stroke="#fff" stroke-width="1"/></svg>
          www.rkvdesignstudio.net
        </li>
      </ul>
    </div>
  </section>
</main>
</body>
</html>
```